Creative & Professional Business Card for hair salon

We are looking to update our business cards. Our salon is creative, modern, progressive and professional and looking for a design that will reflect this.

```html
<!DOCTYPE html>
<html lang="en">
<head>
<meta charset="utf-8">
<title>Silver Lining Studio – Business Card</title>
<link href="https://fonts.googleapis.com/css2?family=Quicksand:wght@300;400&family=Montserrat:ital,wght@0,500;0,600;0,700;1,500&display=swap" rel="stylesheet">
<style>
  :root{
    --stage:#b9b9b9;
    --paper:#ecedee;
    --sky-top:#bcd8ea;
    --brand-slate:#5d8593;
    --card-blue:#87c1e1;
    --wave-light:#a9d3ea;
    --wave-deep:#3ea6d6;
    --box-fill:#e9eaeb;
    --box-edge:#6aaed3;
    --ink-blue:#3f7fa6;
    --white:#ffffff;
    --fb-ink:#1f5f86;
  }
  *{box-sizing:border-box;margin:0;padding:0}
  html,body{width:1200px;height:1018px;overflow:hidden;background:var(--stage)}
  .stage{position:relative;width:1200px;height:1018px}
  .card{position:absolute;top:353px;width:560px;height:312px;overflow:hidden;box-shadow:0 1px 3px rgba(0,0,0,.18)}
  .card--front{left:25px;background:var(--paper)}
  .card--back{left:615px;background:var(--card-blue)}

  /* front */
  .sky{position:absolute;inset:0 0 auto 0;height:120px;
    background:linear-gradient(180deg,var(--sky-top) 0%,rgba(188,216,234,.45) 45%,rgba(236,237,238,0) 100%)}
  .front-name{position:absolute;left:0;right:0;top:150px;text-align:center;
    font-family:'Quicksand',sans-serif;font-weight:300;color:var(--brand-slate);font-size:38px;letter-spacing:-.3px}
  .front-by{position:absolute;left:0;right:0;top:202px;text-align:center;
    font-family:'Quicksand',sans-serif;font-weight:300;color:var(--brand-slate);font-size:20px}

  /* back */
  .back-name{position:absolute;left:25px;top:48px;width:245px;
    font-family:'Quicksand',sans-serif;font-weight:300;color:var(--white);font-size:25px;line-height:1.2}
  .divider{position:absolute;left:284px;top:29px;width:1px;height:76px;background:rgba(255,255,255,.7)}
  .contacts{position:absolute;left:314px;top:29px;list-style:none;
    font-family:'Montserrat',sans-serif;font-weight:500;font-size:12.3px;color:var(--white)}
  .contacts li{display:flex;align-items:center;height:20px}
  .contacts svg{width:11px;height:11px;margin-right:8px;flex:none}
  .appointment{position:absolute;left:23px;top:132px;width:515px;height:140px;
    background:var(--box-fill);border:1px dashed var(--box-edge)}
  .appointment__title{position:absolute;left:0;right:0;top:18px;text-align:center;
    font-family:'Montserrat',sans-serif;font-style:italic;font-weight:500;font-size:12.5px;color:var(--ink-blue)}
  .field{position:absolute;font-family:'Montserrat',sans-serif;font-style:italic;font-weight:500;font-size:13px;color:var(--ink-blue)}
  .rule{position:absolute;border-bottom:1px dotted var(--ink-blue);height:0}
  .wave-band{position:absolute;left:0;right:0;bottom:0;height:52px;
    background:linear-gradient(90deg,var(--wave-light) 0%,var(--card-blue) 55%,var(--wave-deep) 100%)}
  .social{position:absolute;left:14px;top:282px;display:flex;align-items:center;
    font-family:'Montserrat',sans-serif;font-weight:700;font-size:12.8px;color:var(--fb-ink)}
  .social__mark{width:12px;height:12px;background:var(--fb-ink);margin-right:7px;border-radius:1px}
</style>
</head>
<body>
<main class="stage">

  <section class="card card--front">
    <div class="sky" role="img" aria-label="Soft blue sky with light clouds"></div>
    <p class="front-name">Silver Lining Studio</p>
    <p class="front-by">by Jo Marlow</p>
  </section>

  <section class="card card--back">
    <p class="back-name">Silver Lining Studio</p>
    <div class="divider"></div>
    <ul class="contacts">
      <li><svg viewBox="0 0 12 12"><path d="M6 .5a4 4 0 0 0-4 4c0 3 4 7 4 7s4-4 4-7a4 4 0 0 0-4-4zm0 5.6a1.6 1.6 0 1 1 0-3.2 1.6 1.6 0 0 1 0 3.2z" fill="#fff"/></svg>12/40 Harbour Lane, Maroochy</li>
      <li><svg viewBox="0 0 12 12"><path d="M2.4 1l2 .1.9 2.4-1.2 1a6.5 6.5 0 0 0 3.2 3.2l1-1.2 2.4.9.1 2c-.1.6-.6 1-1.2 1A9.4 9.4 0 0 1 1.3 2.2c0-.6.5-1.1 1.1-1.2z" fill="#fff"/></svg>07 5000 1234</li>
      <li><svg viewBox="0 0 12 12"><rect x="1" y="2.5" width="10" height="7" rx=".6" fill="#fff"/><path d="M1.3 3l4.7 3.4L10.7 3" stroke="#87c1e1" stroke-width="1" fill="none"/></svg>salon@silverliningstudio.com.au</li>
      <li><svg viewBox="0 0 12 12"><g fill="none" stroke="#fff" stroke-width=".9"><circle cx="6" cy="6" r="4.8"/><ellipse cx="6" cy="6" rx="2" ry="4.8"/><path d="M1.2 6h9.6"/></g></svg>www.silverliningstudio.com.au</li>
    </ul>

    <div class="appointment">
      <p class="appointment__title">Your Next Appointment is</p>
      <span class="field" style="left:20px;top:45px">For</span>
      <span class="rule" style="left:55px;top:58px;width:440px"></span>
      <span class="field" style="left:20px;top:77px">Date</span>
      <span class="rule" style="left:58px;top:90px;width:182px"></span>
      <span class="field" style="left:261px;top:77px">Time</span>
      <span class="rule" style="left:299px;top:90px;width:196px"></span>
    </div>

    <div class="wave-band" role="img" aria-label="Decorative flowing blue wave band"></div>

    <div class="social"><span class="social__mark"></span>SilverLiningbyJoMarlow</div>
  </section>

</main>
</body>
</html>
```